Financial Planning Firm looking for stationary design using new logo

Need stationary design using our new logo. We are a financial planning firm focused on the planning needs of retirees. Design should incorporate our new logo and its colors. The design should communicate a feeling of stability and security.
Have attached our new logo, as well as our old stationary for reference, letterhead, envelope and business card (but don't rely on for your design). Although the following disclosure must be present on all items "Securities and advisory services offered through Valdimo Advisor Networks LLC, member QUBEX/DLWT. Valdimo is under seperate ownership from any other named entity." in minimum 8 size font. you can see our old stationary for idea of disclosure placement. The business card (front and back) is in the middle of our letterhead sample if it is hard to tell.
Financial

```html
<!DOCTYPE html>
<html lang="en">
<head>
<meta charset="utf-8">
<title>Harlan W. Dreve Financial Group – Stationery</title>
<link href="https://fonts.googleapis.com/css2?family=Crimson+Text:wght@400;600;700&display=swap" rel="stylesheet">
<style>
  :root {
    --backdrop: #d8eefb;
    --paper: #ffffff;
    --navy: #1f4a72;
    --ink: #26384d;
    --mark-fill: #c7ccd9;
    --mark-ring: #dcdcdc;
    --rule: #1f4a72;
  }
  * { margin: 0; padding: 0; box-sizing: border-box; }
  html, body { width: 1200px; height: 817px; overflow: hidden; }
  body {
    background: var(--backdrop);
    position: relative;
    font-family: "Crimson Text", Georgia, serif;
    color: var(--ink);
  }
  .sheet {
    position: absolute;
    background: var(--paper);
    overflow: hidden;
  }
  .brand {
    position: absolute;
    display: flex;
    align-items: center;
    gap: 5px;
  }
  .brand-dot {
    flex: none;
    border-radius: 50%;
    background: var(--navy);
  }
  .brand-name {
    font-weight: 600;
    color: var(--navy);
    line-height: 1.05;
    text-transform: uppercase;
    letter-spacing: 0.02em;
  }
  .emblem {
    position: absolute;
    border-radius: 50%;
    background: var(--mark-fill);
    border-style: solid;
    border-color: var(--mark-ring);
  }
  .center-text { position: absolute; left: 0; right: 0; text-align: center; }

  /* Letterhead */
  .letterhead { left: 145px; top: 108px; width: 423px; height: 600px; }
  .letterhead .brand { left: 127px; top: 20px; }
  .letterhead .brand-dot { width: 30px; height: 30px; }
  .letterhead .brand-name { font-size: 13px; }
  .letterhead .emblem { left: 160px; top: 92px; width: 434px; height: 434px; border-width: 13px; }
  .letterhead .contact { top: 560px; font-size: 5.5px; font-weight: 600; color: var(--navy); }
  .letterhead .footer-rule { position: absolute; left: 20px; right: 20px; top: 572px; border-top: 1px solid var(--rule); }
  .letterhead .disclosure { top: 576px; font-size: 8px; font-weight: 700; color: var(--navy); line-height: 1.15; }

  /* Envelope */
  .envelope { left: 607px; top: 186px; width: 488px; height: 222px; }
  .envelope .brand { left: 21px; top: 18px; }
  .envelope .brand-dot { width: 26px; height: 26px; }
  .envelope .brand-name { font-size: 11px; }
  .envelope .return { position: absolute; left: 21px; top: 50px; font-size: 5px; font-weight: 600; line-height: 1.25; }
  .envelope .emblem { left: 383px; top: 17px; width: 188px; height: 188px; border-width: 6px; }
  .envelope .disclosure { position: absolute; left: 21px; top: 207px; font-size: 4.5px; font-weight: 600; }

  /* Business card front */
  .card-front { left: 672px; top: 466px; width: 168px; height: 101px; }
  .card-front .brand { left: 0; top: 10px; }
  .card-front .brand-dot { width: 12px; height: 12px; }
  .card-front .brand-name { font-size: 5.5px; }
  .card-front .emblem { left: 120px; top: 1px; width: 86px; height: 86px; border-width: 3px; }
  .card-front .details { position: absolute; left: 0; width: 144px; text-align: center; line-height: 1.25; }
  .card-front .person { top: 36px; font-size: 7.5px; font-weight: 700; color: var(--navy); }
  .card-front .role { top: 46px; font-size: 4px; font-weight: 600; }
  .card-front .lines { top: 61px; font-size: 4px; }
  .card-front .rule { position: absolute; left: 0; width: 144px; top: 86px; border-top: 0.5px solid var(--rule); }
  .card-front .note { top: 89px; font-size: 3.2px; }

  /* Business card back */
  .card-back { left: 862px; top: 466px; width: 184px; height: 101px; }
  .card-back .brand-dot { position: absolute; left: 82px; top: 27px; width: 20px; height: 20px; }
  .card-back .disclosure { top: 54px; font-size: 4.5px; font-weight: 700; color: var(--navy); line-height: 1.3; }
</style>
</head>
<body>

  <section class="sheet letterhead" aria-label="Letterhead">
    <div class="emblem" aria-hidden="true"></div>
    <div class="brand">
      <span class="brand-dot"></span>
      <span class="brand-name">Harlan W. Dreve<br>Financial Group, LLC</span>
    </div>
    <p class="center-text contact">555.013.4477 &nbsp;|&nbsp; 555.013.2290 fax &nbsp;• miles@harlandreve.com &nbsp;• www.harlandreve.com &nbsp;• 4120 Harbor Lane, Suite 300, Fairmont, WA 98100</p>
    <div class="footer-rule"></div>
    <p class="center-text disclosure">Securities and advisory services offered through, Valdimo Advisor Networks LLC, member QUBEX/DLWT<br>Valdimo is under separate ownership from any other named entity.</p>
  </section>

  <section class="sheet envelope" aria-label="Envelope">
    <div class="emblem" aria-hidden="true"></div>
    <div class="brand">
      <span class="brand-dot"></span>
      <span class="brand-name">Harlan W. Dreve<br>Financial Group, LLC</span>
    </div>
    <p class="return">4120 Harbor Lane, Suite 300 | Fairmont, WA 98100<br>ADDRESS CORRECTION REQUESTED</p>
    <p class="disclosure">Securities and advisory services offered through Valdimo Advisor Networks LLC, member QUBEX/DLWT</p>
  </section>

  <section class="sheet card-front" aria-label="Business card front">
    <div class="emblem" aria-hidden="true"></div>
    <div class="brand">
      <span class="brand-dot"></span>
      <span class="brand-name">Harlan W. Dreve<br>Financial Group, LLC</span>
    </div>
    <p class="details person">Miles Carver</p>
    <p class="details role">Registered Principal<br>Director of Investment Research and Management</p>
    <p class="details lines">555.013.4477 &nbsp;|&nbsp; 555.013.2290 fax<br>miles@harlandreve.com &nbsp;|&nbsp; www.harlandreve.com<br>4120 Harbor Lane, Suite 300 | Fairmont, WA 98100</p>
    <div class="rule"></div>
    <p class="details note">* Please see back for important disclosures</p>
  </section>

  <section class="sheet card-back" aria-label="Business card back">
    <span class="brand-dot" aria-hidden="true"></span>
    <p class="center-text disclosure">Securities and advisory services offered through<br>Valdimo Advisor Networks LLC, member QUBEX/DLWT<br>Valdimo is under separate ownership from any other named entity.</p>
  </section>

</body>
</html>
```